Need help in designing new business card utilizing our new logo.

BuildMarq Solutions works with Construction Business Owners, Managers & IT Professionals to strengthen software usage and increase user productivity.

Our Construction Accounting and Mobile Field Management Software Clients engage with us in the following areas:

New Software Implementations
Software Re-Implementations
Redesigning Software Usage at the User Level
Project Coordination & Management
Continued Software Support

Old tag line:
Weighing Options - Implementing Solutions

www.buildmarq-solutions.example

Stride 4 is a product, but not needed for a new business card.

```html
<!DOCTYPE html>
<html lang="en">
<head>
<meta charset="utf-8">
<title>BuildMarq Solutions – Business Card</title>
<link rel="stylesheet" href="https://fonts.googleapis.com/css2?family=Arimo:wght@400;700&display=swap">
<style>
  :root {
    --brand-blue: #3442c4;
    --brand-blue-deep: #2834a8;
    --brand-blue-light: #4455d6;
    --paper-white: #f4f5f7;
    --swoosh-grey: #c9ccd4;
    --text-white: #ffffff;
    --stage: #e6e4df;
  }
  * { box-sizing: border-box; margin: 0; padding: 0; }
  html, body { width: 1200px; height: 780px; overflow: hidden; }
  body {
    background: var(--stage);
    font-family: "Arimo", Arial, sans-serif;
    display: flex;
    align-items: center;
    justify-content: center;
    gap: 40px;
  }
  .card {
    position: relative;
    width: 560px;
    height: 320px;
    border-radius: 4px;
    overflow: hidden;
    box-shadow: 0 6px 18px rgba(0,0,0,0.18);
    background: linear-gradient(135deg, var(--brand-blue-light), var(--brand-blue) 50%, var(--brand-blue-deep));
    color: var(--text-white);
  }
  .card-front .swoosh { position: absolute; inset: 0; width: 100%; height: 100%; }
  .wordmark {
    position: absolute;
    display: flex;
    align-items: center;
    gap: 12px;
    font-weight: 700;
    letter-spacing: 0.04em;
    text-transform: uppercase;
    line-height: 1.05;
  }
  .wordmark .mark-square { width: 34px; height: 34px; flex: none; }
  .card-front .wordmark { left: 70px; top: 44px; color: var(--brand-blue); font-size: 26px; }
  .card-front .wordmark .mark-square { background: var(--brand-blue); }
  .wordmark .sub { display: block; font-size: 0.5em; letter-spacing: 0.5em; }
  .social { position: absolute; right: 26px; top: 80px; display: flex; gap: 8px; }
  .social span { width: 22px; height: 22px; border-radius: 50%; background: var(--text-white); }
  .holder { position: absolute; left: 34px; bottom: 40px; }
  .holder .name { font-size: 19px; font-weight: 700; }
  .holder .role { font-size: 13px; margin-top: 2px; }
  .contact {
    position: absolute;
    left: 230px;
    bottom: 20px;
    font-size: 12px;
    line-height: 1.35;
  }
  .contact p + p { margin-top: 7px; }
  .card-back .services {
    position: absolute;
    left: 36px;
    top: 34px;
    list-style: none;
    font-size: 14px;
    line-height: 1.95;
  }
  .card-back .services li { display: flex; align-items: center; gap: 10px; }
  .card-back .services li::before {
    content: "";
    width: 9px; height: 9px;
    background: var(--text-white);
    flex: none;
  }
  .card-back .wordmark { left: 36px; bottom: 40px; color: var(--text-white); font-size: 30px; }
  .card-back .wordmark .mark-square { background: var(--text-white); width: 40px; height: 40px; }
</style>
</head>
<body>
  <section class="card card-front" aria-label="Business card front">
    <svg class="swoosh" viewBox="0 0 560 320" preserveAspectRatio="none" aria-hidden="true">
      <path d="M0 0 H560 V30 C440 30 360 140 230 140 C130 140 60 132 0 142 Z" fill="var(--swoosh-grey)"/>
      <path d="M0 0 H560 V18 C430 18 350 128 230 128 C130 128 60 120 0 130 Z" fill="var(--paper-white)"/>
    </svg>
    <div class="wordmark">
      <span class="mark-square"></span>
      <span>BuildMarq<span class="sub">Solutions</span></span>
    </div>
    <div class="social" aria-label="Social profiles"><span></span><span></span></div>
    <div class="holder">
      <p class="name">Dana R. Whitfield</p>
      <p class="role">Owner</p>
    </div>
    <div class="contact">
      <p>O:800-555-0142 ext.100<br>C:518-555-0193</p>
      <p>dana.whitfield@buildmarq-solutions.example</p>
      <p>14 Maple Row<br>Suite 8<br>Harlow Springs NY 12000</p>
      <p>www.buildmarq-solutions.example</p>
    </div>
  </section>

  <section class="card card-back" aria-label="Business card back">
    <ul class="services">
      <li>New Software Implementations</li>
      <li>Software Re-Implementations</li>
      <li>Redesigning Software Usage at the User Level</li>
      <li>Project Coordination &amp; Management</li>
      <li>Continued Software Support</li>
    </ul>
    <div class="wordmark">
      <span class="mark-square"></span>
      <span>BuildMarq<span class="sub">Solutions</span></span>
    </div>
  </section>
</body>
</html>
```